Velmar Ops Business Cards

We need to design some upbeat business cards. We are an Industrial Rope Access Company/Height Safety Company that specialize in Rope Access, Confined Space, Anchor Points, Safety Systems, PPE Inspecions and Rigging.
Company name is Velmar Ops Ltd
Card is for Gareth Lomas the Company Director
His mobile number is 027 418 9072 and email is gareth@velmarops.co.nz. Website address is www.velmarops.co.nz.
We will post some pictures below to ensure you get a good idea of what we do.

```html
<!DOCTYPE html>
<html lang="en">
<head>
<meta charset="utf-8">
<title>Velmar Ops – Business Cards</title>
<link rel="stylesheet" href="https://fonts.googleapis.com/css2?family=Orbitron:wght@400;700&family=Arimo:wght@400;700&display=swap">
<style>
  :root {
    --stage: #5f6a6a;
    --stage-light: #8a9493;
    --card-white: #ffffff;
    --card-black: #1c1c1c;
    --band: #1f1f1f;
    --ink: #1a1a1a;
    --ghost: #2e2e2e;
    --tab: #f2f2f2;
    --icon: #1d2a5a;
    --service: #d8d8d8;
  }
  * { margin: 0; padding: 0; box-sizing: border-box; }
  html, body { width: 1200px; height: 900px; overflow: hidden; }
  body {
    background: radial-gradient(ellipse at 50% 40%, var(--stage-light), var(--stage) 75%);
    position: relative;
    font-family: "Arimo", Arial, sans-serif;
  }
  .card {
    position: absolute;
    width: 560px;
    height: 320px;
    border-radius: 30px;
    overflow: hidden;
    box-shadow: 0 18px 40px rgba(0,0,0,.35);
  }

  /* Front */
  .card--front { left: 560px; top: 90px; background: var(--card-white); }
  .front__band {
    position: absolute; left: 60px; right: 0; top: 140px; height: 56px;
    background: var(--band);
    display: flex; align-items: center;
  }
  .brand-name {
    font-family: "Orbitron", sans-serif; font-weight: 700;
    color: var(--card-white); font-size: 27px; letter-spacing: .5px;
    padding-left: 18px; width: 270px; white-space: nowrap;
  }
  .front__divider { width: 1px; height: 34px; background: #888; transform: rotate(25deg); margin-right: 22px; }
  .holder { color: var(--card-white); line-height: 1.15; white-space: nowrap; }
  .holder__name { font-weight: 700; font-size: 14px; }
  .holder__role { font-size: 12.5px; }
  .front__contacts {
    position: absolute; left: 60px; right: 16px; top: 208px;
    display: flex; justify-content: space-between; align-items: center;
    font-family: "Orbitron", sans-serif; font-size: 10.5px; color: var(--ink); letter-spacing: .4px;
  }
  .contact { display: flex; align-items: center; gap: 5px; white-space: nowrap; }
  .contact svg { width: 13px; height: 13px; flex: none; }

  /* Back */
  .card--back { left: 80px; top: 480px; background: var(--card-black); }
  .back__wordmark {
    position: absolute; left: 40px; top: 88px;
    font-family: "Orbitron", sans-serif; font-weight: 700;
    font-size: 72px; color: var(--ghost); letter-spacing: 1px; white-space: nowrap;
  }
  .back__services {
    position: absolute; left: 34px; right: 24px; top: 198px;
    font-family: "Orbitron", sans-serif; font-size: 6.3px; letter-spacing: .6px;
    color: var(--service); text-transform: uppercase; white-space: nowrap;
  }
  .tab { position: absolute; width: 20px; height: 48px; background: var(--tab); }
  .tab--left { left: 0; top: 186px; }
  .tab--right { right: 0; top: 44px; }
</style>
</head>
<body>

<section class="card card--front" aria-label="Business card front">
  <div class="front__band">
    <span class="brand-name">Velmar Ops</span>
    <span class="front__divider"></span>
    <div class="holder">
      <div class="holder__name">Gareth Lomas</div>
      <div class="holder__role">Velmar Ops Ltd / Director</div>
    </div>
  </div>
  <div class="front__contacts">
    <span class="contact">
      <svg viewBox="0 0 14 14" aria-hidden="true"><circle cx="7" cy="7" r="7" fill="var(--icon)"/><rect x="4.5" y="3" width="5" height="8" rx="1" fill="none" stroke="#fff" stroke-width="1.1"/></svg>
      (027) 418 9072
    </span>
    <span class="contact">
      <svg viewBox="0 0 14 14" aria-hidden="true"><circle cx="7" cy="7" r="7" fill="var(--icon)"/><rect x="3.5" y="4.5" width="7" height="5" fill="none" stroke="#fff" stroke-width="1"/><path d="M3.5 4.5 7 7.5 10.5 4.5" fill="none" stroke="#fff" stroke-width="1"/></svg>
      gareth@velmarops.co.nz
    </span>
    <span class="contact">
      <svg viewBox="0 0 14 14" aria-hidden="true"><circle cx="7" cy="7" r="7" fill="var(--icon)"/><circle cx="7" cy="7" r="3.8" fill="none" stroke="#fff" stroke-width="1"/><path d="M3.2 7h7.6M7 3.2c-2 2.5-2 5.1 0 7.6M7 3.2c2 2.5 2 5.1 0 7.6" fill="none" stroke="#fff" stroke-width=".8"/></svg>
      www.velmarops.co.nz
    </span>
  </div>
</section>

<section class="card card--back" aria-label="Business card back">
  <span class="tab tab--right"></span>
  <div class="back__wordmark">Velmar Ops</div>
  <p class="back__services">Rope Access - Anchor Points - PPE Certification - Confined Space - Safety Systems - Rigging</p>
  <span class="tab tab--left"></span>
</section>

</body>
</html>
```